Valentine's Day menu

Our establishment on 17, (bar - brasserie - wine bar); Offers a menu for Valentine's Day, one that will be on site and another in delivery.

Menu on site:

Starter: Oysters, warm champagne flambé

Dish: Grilled tournedos, braised endives and Jerusalem artichokes
Ranger Sauce
Sole meunière, lemon sauce, steamed potatoes, rice

Dessert: Tiramisu with red fruits - Flambéed Crêpe Suzette

Menu at 29.90€

Delivery menu: Raclette platter with Savoy cheeses - Pierrade platter and fresh vegetables.
Half-bottle of VERMELLE BLANCS DE BLANS.

Please use the Valentine's Day theme, use our logo and colors (attached). The goal is to get as many reservations as possible.

Reservation required at: 06 52 87 30 19
17
11 rue Honorine Vastel 62780 VALMERY

I remain at your disposal.

- Rate ; 45€ / Person

```html
<!DOCTYPE html>
<html lang="en">
<head>
<meta charset="utf-8">
<title>Brasserie Aubépine – Valentine's Day Menu</title>
<link rel="stylesheet" href="https://fonts.googleapis.com/css2?family=Great+Vibes&family=Josefin+Sans:wght@400&family=Open+Sans:wght@400;600;700&display=swap">
<style>
:root{
  --page:#d9d9d9;
  --wine:#2b1519;
  --glow:#8f1420;
  --gold:#dcaa35;
  --gold-soft:#b9862a;
  --white:#ffffff;
  --text:#f1eaea;
  --ink:#111111;
  --heart-red:#e0313f;
  --heart-dark:#a5161f;
}
*{margin:0;padding:0;box-sizing:border-box}
html,body{width:1200px;height:902px;overflow:hidden;background:var(--page)}
body{position:relative;font-family:"Open Sans",sans-serif;color:var(--text)}
.card{position:absolute;width:394px;height:553px;background:var(--wine);overflow:hidden;box-shadow:0 6px 16px rgba(0,0,0,.25)}
.card--front{left:183px;top:133px;background:radial-gradient(ellipse 190px 150px at 50% 66%,var(--glow) 0%,rgba(80,15,22,.6) 55%,transparent 100%),var(--wine)}
.card--back{left:648px;top:209px}
.center{position:absolute;left:0;width:100%;text-align:center}

/* front */
.brand-name{top:132px;font-family:"Josefin Sans",sans-serif;font-size:34px;color:var(--gold);letter-spacing:1px;line-height:34px}
.brand-tagline{top:207px;font-size:6px;color:var(--white);letter-spacing:.4px}
.flourish{position:absolute;left:92px;width:210px;height:48px;background:linear-gradient(90deg,transparent,var(--gold-soft) 20%,var(--gold) 50%,var(--gold-soft) 80%,transparent);opacity:.55;border-radius:24px}
.flourish--top{top:248px}
.flourish--bottom{top:414px}
.title-script{top:310px;font-family:"Great Vibes",cursive;font-size:46px;color:var(--white);line-height:1}
.title-menu{top:366px;font-size:38px;font-weight:700;color:var(--white);letter-spacing:1px;line-height:1}
.hearts-band{position:absolute;left:0;bottom:0;width:100%;height:95px;background:linear-gradient(180deg,transparent 0%,rgba(224,49,63,.45) 45%,var(--heart-red) 80%,var(--heart-dark) 100%)}

/* back */
.back-header{top:44px;font-family:"Josefin Sans",sans-serif;font-size:21px;color:var(--white);letter-spacing:.5px;line-height:1}
.back-subline{top:70px;font-size:4.5px;color:var(--white);letter-spacing:.3px}
.section-title{position:absolute;left:118px;width:172px;height:30px;border:1.5px solid var(--gold);border-radius:15px;font-family:"Great Vibes",cursive;font-size:22px;color:var(--white);text-align:center;line-height:28px}
.section-title--site{top:107px}
.section-title--delivery{top:339px}
.laurel{position:absolute;width:80px;height:22px;background:linear-gradient(90deg,var(--gold-soft),var(--gold));opacity:.5;border-radius:11px}
.laurel--l{left:36px}
.laurel--r{left:290px}
.laurel--site{top:111px}
.laurel--delivery{top:343px}
.menu-list{position:absolute;left:46px;top:153px;width:210px;font-size:10.5px;line-height:13px;color:var(--text)}
.menu-list dt{font-weight:700;color:var(--white)}
.menu-list dd{margin-bottom:12px}
.delivery-text{position:absolute;left:44px;top:388px;width:235px;font-size:10.5px;line-height:14px}
.price-heart{position:absolute;width:108px;height:108px}
.price-heart svg{position:absolute;inset:0}
.price-heart__label{position:absolute;left:0;width:100%;text-align:center;color:var(--white)}
.price-heart--site{left:274px;top:172px}
.price-heart--delivery{left:274px;top:372px}
.reservation-label{top:473px;font-size:10.5px;color:var(--gold)}
.ribbon{position:absolute;left:36px;top:484px;width:322px;height:44px}
.ribbon svg{position:absolute;inset:0}
.ribbon__phone{position:absolute;left:0;top:11px;width:100%;display:flex;justify-content:center;align-items:center;gap:5px;font-size:17px;font-weight:700;color:var(--ink);line-height:22px}
.address{top:536px;display:flex;justify-content:center;align-items:center;gap:6px;font-size:8.5px;color:var(--text);line-height:11px}
.corner-hearts{position:absolute;bottom:0;height:14px;background:linear-gradient(180deg,transparent,var(--heart-red))}
.corner-hearts--l{left:0;width:40px}
.corner-hearts--r{right:0;width:34px}
</style>
</head>
<body>

<section class="card card--front" aria-label="Front">
  <div class="center brand-name">BRASSERIE<br>AUBÉPINE</div>
  <div class="center brand-tagline">BAR BRASSERIE - COCKTAILS - BIÈRE - CHAMPAGNE - VINS</div>
  <div class="flourish flourish--top" role="img" aria-label="Gold flourish ornament with a heart"></div>
  <div class="center title-script">Valentine's Day</div>
  <div class="center title-menu">MENU</div>
  <div class="flourish flourish--bottom" role="img" aria-label="Gold flourish ornament with a heart"></div>
  <div class="hearts-band" role="img" aria-label="Scattered red and white hearts"></div>
</section>

<section class="card card--back" aria-label="Back">
  <div class="center back-header">BRASSERIE AUBÉPINE</div>
  <div class="center back-subline">BAR BRASSERIE &nbsp;·&nbsp; COCKTAILS - BIÈRE - CHAMPAGNE - VINS</div>

  <div class="laurel laurel--l laurel--site" role="img" aria-label="Gold laurel branch"></div>
  <div class="laurel laurel--r laurel--site" role="img" aria-label="Gold laurel branch"></div>
  <div class="section-title section-title--site">Menu on site:</div>

  <dl class="menu-list">
    <dt>Starter:</dt>
    <dd>Oysters, warm champagne flambé</dd>
    <dt>Dish:</dt>
    <dd>Grilled tournedos, braised endives and Jerusalem artichokes , Ranger Sauce<br>Sole meunière, lemon sauce, steamed potatoes, rice</dd>
    <dt>Dessert:</dt>
    <dd>Tiramisu with red fruits - Flambéed Crêpe Suzette</dd>
  </dl>

  <div class="price-heart price-heart--site">
    <svg viewBox="0 0 100 100"><path d="M50 95C20 70 4 52 4 30 4 14 16 4 30 4 40 4 47 11 50 19 53 11 60 4 70 4 84 4 96 14 96 30 96 52 80 70 50 95Z" fill="none" stroke="#cbb" stroke-width="1" stroke-dasharray="2 2"/></svg>
    <div class="price-heart__label" style="top:34px;font-size:12px">Menu at</div>
    <div class="price-heart__label" style="top:51px;font-size:14px;font-weight:700">29.90€</div>
  </div>

  <div class="laurel laurel--l laurel--delivery" role="img" aria-label="Gold laurel branch"></div>
  <div class="laurel laurel--r laurel--delivery" role="img" aria-label="Gold laurel branch"></div>
  <div class="section-title section-title--delivery">Delivery menu:</div>

  <p class="delivery-text">Raclette platter with Savoy cheeses -<br>Pierrade platter and fresh vegetables.<br>Half-bottle of VERMELLE BLANCS DE BLANS.</p>

  <div class="price-heart price-heart--delivery">
    <svg viewBox="0 0 100 100"><path d="M50 95C20 70 4 52 4 30 4 14 16 4 30 4 40 4 47 11 50 19 53 11 60 4 70 4 84 4 96 14 96 30 96 52 80 70 50 95Z" fill="none" stroke="#cbb" stroke-width="1" stroke-dasharray="2 2"/></svg>
    <div class="price-heart__label" style="top:28px;font-size:12px">Rate :</div>
    <div class="price-heart__label" style="top:44px;font-size:15px;font-weight:700">45€</div>
    <div class="price-heart__label" style="top:64px;font-size:11px">/ Person</div>
  </div>

  <div class="center reservation-label">Reservation required at:</div>
  <div class="ribbon">
    <svg viewBox="0 0 322 44" width="322" height="44">
      <polygon points="0,4 66,10 66,34 12,30 22,17" fill="#ffffff"/>
      <polygon points="322,4 256,10 256,34 310,30 300,17" fill="#ffffff"/>
      <rect x="48" y="8" width="226" height="30" rx="14" fill="#ffffff" stroke="#2b1519" stroke-width="1.5"/>
    </svg>
    <div class="ribbon__phone">
      <svg width="14" height="14" viewBox="0 0 24 24"><circle cx="12" cy="12" r="10.5" fill="none" stroke="#111" stroke-width="2"/><path d="M8.5 7c.6-.6 1.2-.5 1.5 0l1 1.7c.3.5.1 1-.3 1.3l-.6.5c.6 1.3 1.5 2.2 2.8 2.8l.5-.6c.3-.4.8-.6 1.3-.3l1.7 1c.5.3.6.9 0 1.5-1 1-2.3 1.2-4 .3-1.7-1-3.1-2.4-4-4-.9-1.8-.7-3.1.1-4.2Z" fill="#111"/></svg>
      <span>06 52 87 30 19</span>
    </div>
  </div>
  <div class="center address">
    <svg width="9" height="11" viewBox="0 0 12 16"><path d="M6 0C2.7 0 0 2.6 0 5.9 0 10 6 16 6 16s6-6 6-10.1C12 2.6 9.3 0 6 0Zm0 8.3A2.3 2.3 0 1 1 6 3.7a2.3 2.3 0 0 1 0 4.6Z" fill="#f1eaea"/></svg>
    <span>11 rue Honorine Vastel 62780 VALMERY</span>
  </div>
  <div class="corner-hearts corner-hearts--l" role="img" aria-label="Small red hearts"></div>
  <div class="corner-hearts corner-hearts--r" role="img" aria-label="Small red hearts"></div>
</section>

</body>
</html>
```